Stationary Design For New Dynamic Company

Hi there we require stationary designed for our new company, we have used "Pixel Harbor" recently for our logo and were very impressed with all of the designers that contributed towards the final result.
What we require now is the following:
Letter head layout (A4)
Business Cards (5 people)
With Compliments slips
Envelopes
Email stationary
We would like to use our current logo design and I have included it for your use (JPEG is the one we have chosen and I have attached an EPS file for your use). Our company specializes in architectural cladding and our products are used by architects, builders and private clients, so we wish for the stationary to be suitable and attractive to our clientele.
I thank everyone in advance for your contributions.
Thank you to all that have provided your designs for this project, I apologize for not providing feedback as I have been away. I have looked at everyone's designs and they all look great and I will come back to those designers that I wish to have changes made sometime today.
Once again a big thank you to all involved.
Business

```html
<!DOCTYPE html>
<html lang="en">
<head>
<meta charset="utf-8">
<title>Stonevale Email Signature</title>
<link href="https://fonts.googleapis.com/css2?family=Arimo:wght@400;700&display=swap" rel="stylesheet">
<style>
  :root {
    --navy: #163f66;
    --orange: #f0901e;
    --ink: #2b2b2b;
    --grey: #555a5f;
    --rule: #cfd2d5;
    --paper: #ffffff;
    --social-1: #3b5998;
    --social-2: #8a8f95;
    --social-3: #2fa4d8;
    --social-4: #c4302b;
    --social-5: #1f78b4;
  }
  * { box-sizing: border-box; margin: 0; padding: 0; }
  html, body { width: 1200px; height: 900px; overflow: hidden; background: var(--paper); }
  body { font-family: "Arimo", Arial, sans-serif; color: var(--ink); position: relative; }

  .masthead {
    position: absolute; top: 70px; left: 60px; width: 1080px; height: 50px;
    display: flex; align-items: flex-start; gap: 18px;
  }
  .band { position: relative; margin-top: 12px; height: 20px; background: var(--navy); flex-shrink: 0; }
  .band::after { content: ""; position: absolute; left: 0; right: 0; top: 24px; height: 4px; background: var(--orange); }
  .band--short { width: 52px; }
  .band--long { flex: 1 1 auto; }
  .brand { display: flex; align-items: center; gap: 8px; height: 44px; flex-shrink: 0; }
  .brand__square { width: 20px; height: 20px; background: var(--orange); }
  .brand__name { font-size: 21px; font-weight: 700; color: var(--navy); letter-spacing: 0.3px; white-space: nowrap; }

  .signature { position: absolute; left: 72px; top: 420px; width: 500px; font-size: 13px; color: var(--grey); }
  .signoff { margin-bottom: 30px; }
  .person__name { font-weight: 700; color: var(--ink); }
  .person__role { margin-top: 4px; }
  .contacts { list-style: none; margin-top: 24px; }
  .contacts li { display: flex; align-items: center; gap: 10px; height: 21px; }
  .contacts__tag { width: 15px; height: 15px; background: var(--orange); color: #fff; font-size: 10px; font-weight: 700; display: flex; align-items: center; justify-content: center; }
  .divider { margin: 22px 0 12px; height: 2px; background: var(--rule); }
  .footer-note { line-height: 20px; font-size: 12.5px; }
  .social { display: flex; gap: 10px; margin-top: 10px; }
  .social span { width: 18px; height: 18px; border-radius: 3px; }
  .social .s1 { background: var(--social-1); }
  .social .s2 { background: var(--social-2); }
  .social .s3 { background: var(--social-3); }
  .social .s4 { background: var(--social-4); }
  .social .s5 { background: var(--social-5); }
</style>
</head>
<body>
  <header class="masthead">
    <div class="band band--short"></div>
    <div class="brand">
      <span class="brand__square"></span>
      <span class="brand__name">STONEVALE</span>
    </div>
    <div class="band band--long"></div>
  </header>

  <section class="signature">
    <p class="signoff">Kind reagds,</p>
    <p class="person__name">Alan Brooks</p>
    <p class="person__role">Sales,Marketing &amp; Customer</p>
    <ul class="contacts">
      <li><span class="contacts__tag">P</span>555-0148-2231</li>
      <li><span class="contacts__tag">E</span>a.brooks@stonevale.com</li>
      <li><span class="contacts__tag">W</span>http://www.stonevale.com</li>
    </ul>
    <div class="divider"></div>
    <p class="footer-note">This Message wae sent by&nbsp; Alan Brooks<br>If you realy want to Knom more about me, you can visite my social services profiles</p>
    <div class="social" aria-label="Social profiles">
      <span class="s1"></span><span class="s2"></span><span class="s3"></span><span class="s4"></span><span class="s5"></span>
    </div>
  </section>
</body>
</html>
```